Brelton Services - Fast, Efficient and Gas Mainteance for Domestic, Commercial and Industrial clients

We are in the process of purchasing a new business and would like to get a new logo and business card.
Business is a gas maintenance business that also does new gas installations.
Has been established since 1988.
Services include:
Install all types of gas appliances & equipment inc. hot water units
Maintain / repair / replace all types of gas appliances & equipment

Target Market(s)

Domestic, Commercial and Industrial clients

Industry/Entity Type

Business

Contact Information for Business Card

admin@breltonservices.example.au
07 5382 4690
Brelton Services PTY LTD

Logo Text

Gas Fitting & Plumbing Maintenance Specialists

Font styles to use
Sans Serif

Requirements
Must have
• Logo
• Business name, contact number, email address, web address
• Domestic | Commercial | Industrial Est Since 1988
Nice to have
• Possibly a black card with a flame logo to one side
Should not have
• Spelling errors

```html
<!DOCTYPE html>
<html lang="en">
<head>
<meta charset="utf-8">
<title>Brelton Services – Business Card</title>
<link href="https://fonts.googleapis.com/css2?family=Roboto:wght@400;500;700;900&display=swap" rel="stylesheet">
<style>
  :root {
    --page-bg: #e9e9e7;
    --card-black: #050505;
    --flame-yellow: #f5b400;
    --flame-orange: #f07a1a;
    --flame-red: #e0201e;
    --brand-red: #d62a2a;
    --ink-dark: #1a1a1a;
    --ink-light: #ffffff;
  }
  * { box-sizing: border-box; margin: 0; padding: 0; }
  html, body {
    width: 1200px;
    height: 857px;
    overflow: hidden;
    background: var(--page-bg);
    font-family: "Roboto", Arial, sans-serif;
  }
  .sheet {
    position: relative;
    width: 1200px;
    height: 857px;
    display: flex;
    align-items: center;
    justify-content: center;
    gap: 40px;
  }
  .card {
    position: relative;
    width: 540px;
    height: 300px;
    border-radius: 34px;
    overflow: hidden;
    box-shadow: 0 10px 24px rgba(0,0,0,0.18);
  }

  /* Front: black logo side */
  .card--logo {
    background: var(--card-black);
    display: flex;
    align-items: center;
    justify-content: center;
  }
  .brand-lockup {
    display: flex;
    align-items: center;
    gap: 16px;
  }
  .brand-dot {
    width: 40px;
    height: 40px;
    border-radius: 50%;
    background: var(--flame-orange);
  }
  .brand-name {
    font-weight: 500;
    font-size: 46px;
    letter-spacing: 1px;
    color: var(--brand-red);
  }

  /* Back: gradient details side */
  .card--details {
    background:
      radial-gradient(ellipse 70% 80% at 45% 100%, rgba(225,30,30,0.55), rgba(225,30,30,0) 70%),
      linear-gradient(172deg, var(--flame-yellow) 0%, var(--flame-orange) 45%, var(--flame-red) 85%);
    color: var(--ink-dark);
  }
  .company {
    position: absolute;
    top: 92px;
    right: 56px;
    text-align: center;
    width: 300px;
  }
  .company__name {
    font-weight: 900;
    font-size: 30px;
    letter-spacing: 0.5px;
    text-transform: uppercase;
    line-height: 1;
  }
  .company__suffix {
    font-weight: 700;
    font-size: 10px;
    letter-spacing: 1px;
    margin-top: 2px;
  }
  .company__rule {
    height: 1.5px;
    background: var(--ink-dark);
    margin-top: 6px;
  }
  .sectors {
    position: absolute;
    left: 26px;
    right: 22px;
    bottom: 50px;
    display: flex;
    align-items: center;
    justify-content: space-between;
    font-size: 15.5px;
    font-weight: 400;
    text-transform: uppercase;
    color: var(--ink-dark);
    border-bottom: 1.5px solid var(--ink-dark);
    padding-bottom: 3px;
  }
  .sectors__sep {
    width: 7px;
    height: 7px;
    border-radius: 50%;
    background: var(--ink-light);
    display: inline-block;
  }
  .contacts {
    position: absolute;
    left: 26px;
    right: 22px;
    bottom: 24px;
    display: flex;
    justify-content: space-between;
    align-items: center;
    font-size: 12.5px;
    color: var(--ink-light);
  }
  .contact {
    display: flex;
    align-items: center;
    gap: 5px;
    white-space: nowrap;
  }
  .contact--phone { font-weight: 700; }
  .contact svg { width: 12px; height: 12px; flex: none; }
</style>
</head>
<body>
<main class="sheet">
  <section class="card card--logo" aria-label="Card front">
    <div class="brand-lockup">
      <span class="brand-dot" aria-hidden="true"></span>
      <span class="brand-name">Brelton</span>
    </div>
  </section>

  <section class="card card--details" aria-label="Card back">
    <div class="company">
      <h1 class="company__name">Brelton Services</h1>
      <p class="company__suffix">PTY. LTD.</p>
      <div class="company__rule"></div>
    </div>

    <p class="sectors">
      <span>Domestic</span><span class="sectors__sep"></span>
      <span>Commercial</span><span class="sectors__sep"></span>
      <span>Industrial</span>
      <span>Est Since 1988</span>
    </p>

    <div class="contacts">
      <span class="contact contact--email">
        <svg viewBox="0 0 12 12" aria-hidden="true"><circle cx="6" cy="6" r="6" fill="#fff"/><rect x="3" y="4" width="6" height="4" fill="none" stroke="#d62a2a" stroke-width="0.9"/><path d="M3 4 L6 6.3 L9 4" fill="none" stroke="#d62a2a" stroke-width="0.9"/></svg>
        admin@breltonservices.example.au
      </span>
      <span class="contact contact--phone">
        <svg viewBox="0 0 12 12" aria-hidden="true"><circle cx="6" cy="6" r="6" fill="#fff"/><path d="M4 3.2 L5 3 L5.6 4.6 L4.9 5.1 Q5.5 6.5 6.9 7.1 L7.4 6.4 L9 7 L8.8 8 Q8.5 8.8 7.5 8.7 Q4 8 3.3 4.5 Q3.2 3.5 4 3.2 Z" fill="#d62a2a"/></svg>
        07 5382 4690
      </span>
      <span class="contact contact--web">
        <svg viewBox="0 0 12 12" aria-hidden="true"><circle cx="6" cy="6" r="6" fill="#fff"/><circle cx="6" cy="6" r="3.2" fill="none" stroke="#d62a2a" stroke-width="0.8"/><path d="M2.8 6 H9.2 M6 2.8 Q4.3 6 6 9.2 Q7.7 6 6 2.8" fill="none" stroke="#d62a2a" stroke-width="0.7"/></svg>
        breltonservices.example.au
      </span>
    </div>
  </section>
</main>
</body>
</html>
```